Create a Magazine Ad for an asbestos law firm

we need an 8 X 13 ad to be on the back of a magazine cover. We have the text Attached and want a similar look and feel to our website : www.harborvale-claims.example. The ad should be targeted to white males 55 years or older who are conservative and worked in industry or industrial plants. The main offer is a free case review and trying to get them to call the telephone number.

Target Market(s)

White collar men who worked in industrial plants. Age 55 years or older.

Industry/Entity Type

Legal

Requirements
Must have
• Pictures of white middle class conservative man or man and woman
Nice to have
• look at www.harborvale-claims.example to an. idea of what we are looking for

```html
<!DOCTYPE html>
<html lang="en">
<head>
<meta charset="utf-8">
<title>Harborvale Claims – Mesothelioma Compensation Ad</title>
<link href="https://fonts.googleapis.com/css2?family=Oswald:wght@500;600;700&family=Montserrat:wght@400;500;600;700&display=swap" rel="stylesheet">
<style>
  :root{
    --teal:#2a7d92;
    --teal-dark:#1f6779;
    --teal-text:#1d6f84;
    --yellow:#f5c518;
    --cream:#f4f1e6;
    --white:#ffffff;
    --photo-grey:#9a9a9a;
    --photo-light:#d6d6d6;
  }
  *{margin:0;padding:0;box-sizing:border-box}
  html,body{width:738px;height:1200px;overflow:hidden;background:var(--teal)}
  .ad{position:relative;width:738px;height:1200px;overflow:hidden;
      background:radial-gradient(ellipse at 60% 40%,#318aa0 0%,var(--teal) 55%,var(--teal-dark) 100%);
      font-family:'Montserrat',sans-serif;color:var(--white)}
  .abs{position:absolute;white-space:nowrap}

  /* Headline panel */
  .headline-panel{left:28px;top:0;width:334px;height:408px}
  .brand{left:80px;top:38px;display:flex;align-items:center;gap:8px}
  .brand-dot{width:26px;height:26px;border-radius:50%;background:var(--white)}
  .brand-name{font-weight:600;font-size:21px;color:var(--white);line-height:1}
  .brand-tag{left:114px;top:66px;font-size:6.5px;font-weight:600;color:var(--white)}
  .headline{left:28px;width:334px;text-align:center;color:var(--teal-text)}
  .kicker{font-weight:700;letter-spacing:3.6px;font-size:14.5px;line-height:1}
  .kicker-1{top:131px}
  .kicker-2{top:226px;font-size:13px;letter-spacing:3px}
  .big{font-family:'Oswald',sans-serif;font-weight:700;line-height:1;text-transform:uppercase}
  .big-1{top:146px;font-size:48px}
  .big-2{top:236px;font-size:44px}
  .rule{left:88px;top:208px;width:214px;height:2px;background:var(--white)}

  /* Right intro */
  .accent-bar{left:380px;top:31px;width:38px;height:5px;background:var(--yellow)}
  .intro{left:378px;top:42px;font-size:19px;line-height:23px;font-weight:500}
  .bullets{list-style:none}
  .bullets li{position:relative;padding-left:20px;font-weight:700;font-size:16.5px;line-height:20.5px}
  .bullets li::before{content:"";position:absolute;left:2px;top:7px;width:7px;height:7px;border-radius:50%;background:var(--yellow)}
  .list-1{left:378px;top:170px}
  .list-1 li{margin-bottom:7px}
  .help{left:381px;top:262px;font-size:14.5px;line-height:17px}
  .list-2{left:378px;top:314px}
  .list-2 li{margin-bottom:8px}

  /* Trust fund */
  .trust{left:28px;top:478px;display:flex;align-items:flex-start;gap:8px}
  .trust-num{font-family:'Oswald',sans-serif;font-weight:700;font-size:52px;color:var(--yellow);line-height:1}
  .trust-text{font-weight:700;font-size:17px;line-height:24px;padding-top:4px}
  .trust-body{left:28px;top:541px;font-size:15.3px;line-height:24px}

  /* Photo area */
  .photos{left:0;top:650px;width:330px;height:550px}

  /* Settlements */
  .settle-head{left:337px;top:641px;color:var(--yellow);font-weight:700;font-size:18.5px;line-height:24px}
  .settle-body{left:339px;top:700px;font-size:15.2px;line-height:20.5px}
  .amount-num{font-family:'Oswald',sans-serif;font-weight:600;font-size:30px;color:var(--yellow);line-height:1.05}
  .amount-num.tight{letter-spacing:-.6px}
  .amount-note{font-size:10px;line-height:1.15;margin-top:3px}
  .divider{width:2px;height:20px;background:var(--white)}
  .eligible{left:342px;top:1086px;font-size:10.5px;font-weight:700;line-height:1}
  .eligible .free{font-family:'Oswald',sans-serif;color:var(--yellow);font-size:31px;line-height:1}
  .eligible-sub{left:342px;top:1117px;font-size:10.6px;line-height:1}

  /* Call to action */
  .cta{left:340px;top:1144px;width:398px;height:56px}
  .cta-top{left:388px;top:1147px;width:304px;text-align:center;font-size:10.8px;font-weight:700;color:var(--teal-text);letter-spacing:.3px;line-height:1.2}
  .phone{left:440px;top:1164px;display:flex;align-items:center;gap:8px;font-family:'Oswald',sans-serif;font-weight:700;font-size:26px;color:var(--white);letter-spacing:3px;line-height:1.15}
</style>
</head>
<body>
<main class="ad">

  <svg class="abs headline-panel" viewBox="0 0 334 408" aria-hidden="true">
    <path d="M0 0H334V318Q334 408 167 408Q0 408 0 318Z" fill="var(--yellow)"/>
  </svg>
  <div class="abs brand"><span class="brand-dot"></span><span class="brand-name">Harborvale Claims</span></div>
  <p class="abs brand-tag">Over 20 years of fighting for mesothelioma patients and families</p>

  <p class="abs headline kicker kicker-1">DIAGNOSED WITH</p>
  <h1 class="abs headline big big-1">Mesothelioma,</h1>
  <div class="abs rule"></div>
  <p class="abs headline kicker kicker-2">YOU COULD BE OWED</p>
  <h2 class="abs headline big big-2">Compensation</h2>

  <div class="abs accent-bar"></div>
  <p class="abs intro">It's very likely you developed this<br>disease through asbestos exposure.<br>Mesothelioma patients are getting<br>multi-million dollar settlements,<br>decades later, from:</p>
  <ul class="abs bullets list-1">
    <li>Exposure to asbestos products,</li>
    <li>Ex-employers, or</li>
    <li>Talcum baby powder companies.</li>
  </ul>
  <p class="abs help">We can help you find out if you qualify<br>for a case in minutes.</p>
  <ul class="abs bullets list-2">
    <li>We'll analyze your situation<br>at no cost</li>
    <li>Determine how much<br>compensation you could be<br>entitled too</li>
    <li>Show you the next steps<br>to get what you're owed</li>
  </ul>

  <div class="abs trust">
    <span class="trust-num">$30</span>
    <span class="trust-text">Billion is Available in<br>Trust for Mesothelioma Patients</span>
  </div>
  <p class="abs trust-body">Tradesmen in many industries were negligently exposed to asbestos materials well into<br>the 1990s. Whether you developed Mesothelioma yourself due to asbestos exposure<br>or you're the surviving family of a lost loved one you could be<br>entitled to significant compensation.</p>

  <svg class="abs photos" viewBox="0 0 330 550" role="img" aria-label="Circular black-and-white photos of an older man with glasses and a doctor reviewing a chart with a patient">
    <defs>
      <linearGradient id="photoTone" x1="0" y1="0" x2="1" y2="1">
        <stop offset="0" stop-color="var(--photo-light)"/>
        <stop offset="1" stop-color="var(--photo-grey)"/>
      </linearGradient>
    </defs>
    <circle cx="-13" cy="119" r="115" fill="url(#photoTone)" stroke="var(--white)" stroke-width="4"/>
    <circle cx="141" cy="413" r="167" fill="url(#photoTone)" stroke="var(--teal-dark)" stroke-width="6"/>
    <circle cx="199" cy="144" r="102" fill="url(#photoTone)" stroke="var(--teal-dark)" stroke-width="8"/>
  </svg>

  <h3 class="abs settle-head">How much Money Can People<br>Receive from a Mesothelioma Case?</h3>
  <p class="abs settle-body">Depending on where you were exposed and<br>a few other factors, you can get a settlement<br>from 6 to 7 figures. Here are a few examples<br>of Mesothelioma Settlements received by our<br>clients. These figures are the total<br>compensation after all attorney fees and<br>expenses are deducted</p>

  <div class="abs" style="left:339px;top:866px"><div class="amount-num">$6,142,500</div><div class="amount-note">Exposed through heavy<br>duty vehicles</div></div>
  <div class="abs divider" style="left:526px;top:874px"></div>
  <div class="abs" style="left:575px;top:866px"><div class="amount-num">$6,033,510</div><div class="amount-note">Exposed through general<br>contracting</div></div>

  <div class="abs" style="left:339px;top:943px"><div class="amount-num">$5,939,010</div><div class="amount-note">Exposed through boat repair</div></div>
  <div class="abs divider" style="left:526px;top:951px"></div>
  <div class="abs" style="left:575px;top:943px"><div class="amount-num">$3,921,750</div><div class="amount-note">Exposed through navy<br>service</div></div>

  <div class="abs" style="left:339px;top:1020px"><div class="amount-num">$3,600,450</div><div class="amount-note">Exposed through navy service</div></div>
  <div class="abs divider" style="left:526px;top:1028px"></div>
  <div class="abs" style="left:575px;top:1020px"><div class="amount-num tight">$2.5 MILLION</div><div class="amount-note">Exposed from Brightwell Talcum<br>Baby Powder.</div></div>

  <p class="abs eligible">Find out if you're Eligible, for <span class="free">FREE</span> , in Minutes</p>
  <p class="abs eligible-sub">We'll evaluate your situation and tell you what your case could be worth</p>

  <svg class="abs cta" viewBox="0 0 398 56" aria-hidden="true">
    <polygon points="48,0 398,0 398,18 40,18" fill="var(--cream)"/>
    <polygon points="40,18 398,18 398,56 20,56" fill="var(--yellow)"/>
    <g fill="var(--cream)">
      <polygon points="30,0 40,0 18,30 8,30"/>
      <polygon points="14,0 22,0 0,30 -8,30"/>
    </g>
  </svg>
  <p class="abs cta-top">GET YOUR FREE EVALUATION NOW!</p>
  <div class="abs phone">
    <svg width="24" height="24" viewBox="0 0 24 24" aria-hidden="true">
      <path fill="var(--white)" d="M6.6 10.8a15.1 15.1 0 0 0 6.6 6.6l2.2-2.2c.3-.3.7-.4 1-.2 1.1.4 2.3.6 3.6.6.6 0 1 .4 1 1V20c0 .6-.4 1-1 1A17 17 0 0 1 3 4c0-.6.4-1 1-1h3.5c.6 0 1 .4 1 1 0 1.3.2 2.5.6 3.6.1.3 0 .7-.2 1Z"/>
    </svg>
    <span>1-XXX-XXXX</span>
  </div>

</main>
</body>
</html>
```